Business Card Tech Company
Veradon Corp
Project: Business Card Tech Company
Business Card Tech Company -
Creative Brief
Simple
Marcel Dufresne
CEO
2745 Rue Belcourt, Québec, QC G2K 3P7, Canada
mdufresne@veradoncorp-example.com
www.veradoncorp-example.com
You can add Twitter @veradoncorp We are very open to different designs, We will provide fast feedback, You can try many styles and many fonts, Right now, our slogan is: the world made yours. You can put it on some designs if it fits well, consider we might want to change it.
We would like a back mostly visual, without much info.

```html
<!DOCTYPE html>
<html lang="en">
<head>
<meta charset="UTF-8">
<title>Veradon Corp — Business Card</title>
<link href="https://fonts.googleapis.com/css2?family=Ubuntu:wght@400;500;700&display=swap" rel="stylesheet">
<style>
  :root {
    --bg: #ecebe8;
    --card: #ffffff;
    --brand-blue: #1b6db5;
    --deep-blue: #16579a;
    --swoosh-grey: #8a8d91;
    --text-grey: #5d6066;
    --rule: #c9cbce;
  }
  * { margin: 0; padding: 0; box-sizing: border-box; }
  html, body {
    width: 1200px; height: 780px; overflow: hidden;
    background: var(--bg);
    font-family: "Ubuntu", sans-serif;
  }
  .card {
    position: absolute; left: 75px; top: 90px;
    width: 1050px; height: 600px;
    background: var(--card);
    border-radius: 34px;
    overflow: hidden;
    box-shadow: 0 10px 30px rgba(0,0,0,0.12);
  }
  .swoosh { position: absolute; left: 0; top: 0; width: 1050px; height: 600px; }
  .brand {
    position: absolute; left: 240px; top: 105px;
    display: flex; align-items: center; gap: 26px;
  }
  .brand-dot {
    width: 120px; height: 120px; border-radius: 50%;
    background: var(--brand-blue);
  }
  .brand-name {
    font-size: 112px; font-weight: 500; color: var(--brand-blue);
    letter-spacing: 1px; line-height: 1;
  }
  .identity {
    position: absolute; right: 530px; top: 305px;
    text-align: right; color: var(--text-grey);
    font-size: 20px; line-height: 1.45;
  }
  .identity .name { font-size: 28px; font-weight: 700; color: var(--deep-blue); }
  .identity .role { margin-bottom: 14px; }
  .divider {
    position: absolute; left: 545px; top: 305px;
    width: 2px; height: 200px; background: var(--rule);
  }
  .contacts {
    position: absolute; left: 568px; top: 305px;
    list-style: none; color: var(--text-grey); font-size: 19px;
  }
  .contacts li { display: flex; align-items: center; gap: 14px; height: 38px; }
  .contacts svg { width: 22px; height: 22px; flex: none; }
  .plain-dot { width: 20px; height: 20px; border-radius: 50%; background: var(--brand-blue); margin: 0 1px; flex: none; }
</style>
</head>
<body>
  <div class="card">
    <svg class="swoosh" viewBox="0 0 1050 600" aria-hidden="true">
      <path d="M0,140 C70,250 110,430 235,600 L0,600 Z" fill="var(--swoosh-grey)"/>
      <path d="M0,150 C60,260 95,440 200,600 L0,600 Z" fill="#ffffff"/>
      <path d="M0,175 C50,280 80,450 175,600 L0,600 Z" fill="var(--brand-blue)"/>
    </svg>

    <div class="brand">
      <div class="brand-dot"></div>
      <div class="brand-name">Veradon</div>
    </div>

    <div class="identity">
      <div class="name">Marcel Dufresne</div>
      <div class="role">CEO</div>
      <div>2745 Rue Belcourt,</div>
      <div>Québec, QC, G2K 3P7, Canada</div>
    </div>

    <div class="divider"></div>

    <ul class="contacts">
      <li>
        <svg viewBox="0 0 24 24"><rect x="6" y="2" width="12" height="20" rx="2" fill="var(--brand-blue)"/><rect x="8" y="5" width="8" height="11" fill="#fff"/><circle cx="12" cy="19" r="1.2" fill="#fff"/></svg>
        418-555-0142
      </li>
      <li>
        <svg viewBox="0 0 24 24"><rect x="2" y="5" width="20" height="14" rx="2" fill="var(--brand-blue)"/><path d="M3 6 L12 13 L21 6" stroke="#fff" stroke-width="2" fill="none"/></svg>
        mdufresne@veradoncorp-example.com
      </li>
      <li>
        <svg viewBox="0 0 24 24"><circle cx="12" cy="12" r="10" fill="var(--brand-blue)"/><ellipse cx="12" cy="12" rx="4" ry="10" stroke="#fff" stroke-width="1.5" fill="none"/><path d="M2 12 H22 M4 7 H20 M4 17 H20" stroke="#fff" stroke-width="1.3"/></svg>
        www.veradoncorp-example.com
      </li>
      <li>
        <span class="plain-dot"></span>
        @veradoncorp
      </li>
    </ul>
  </div>
</body>
</html>
```